International Sex Coach needs a Book Cover in less than 3 days

I need a cover design for my book coming out next week titled "A Quiet Atlas Toward Closeness". The book explores the origins of our cultural ideas about sexuality and taboo and is interwoven with personal memoir.
The reader must feel that they are being pulled into an intimate sexual story, but also a deeper understanding of sex itself. Like they are jumping into bed with me, you might say. I would like the title to take up the majority of the space over an image of 3D, very real bed sheets, but I am open to your ideas. I haven't purchased any images yet, but there are a few below I was drawn to.
In its essence, this book is designed to reeducate the reader about sexuality and open them up to a new paradigm of sexual wellness.
The author name is Mirela Oswin. Page must also include the phrase: a revolutionary new approach to sexuality, relationship and love.
Size 6" x 9" (15.24 x 22.86 cm)
Thanks!

Reason: I need more time to review the designs and give feedback.

Target Market(s)

Sexually active men and women.

Industry/Entity Type

Wellness

Font styles to use
Serif

```html
<!DOCTYPE html>
<html lang="en">
<head>
<meta charset="utf-8">
<title>A Quiet Atlas Toward Closeness — Mirela Oswin</title>
<link rel="stylesheet" href="https://fonts.googleapis.com/css2?family=Bebas+Neue&display=swap">
<style>
  :root {
    --sheet-crimson: #8f1a3c;
    --sheet-crimson-deep: #6a0f2a;
    --sheet-crimson-light: #a8304f;
    --sheet-lavender: #8a6e9a;
    --sheet-lavender-light: #a08bb0;
    --title-white: #ffffff;
    --ink-black: #111111;
  }
  html, body {
    margin: 0;
    padding: 0;
    width: 800px;
    height: 1200px;
    overflow: hidden;
    background: #ffffff;
  }
  .cover {
    position: relative;
    width: 800px;
    height: 1200px;
    overflow: hidden;
    font-family: "Bebas Neue", "Oswald", sans-serif;
    text-align: center;
  }
  .cover-photo {
    position: absolute;
    inset: 0;
    background:
      radial-gradient(ellipse 60% 18% at 50% 78%, rgba(217,169,138,0.55), rgba(217,169,138,0) 70%),
      linear-gradient(180deg,
        var(--sheet-crimson-light) 0%,
        var(--sheet-crimson) 22%,
        var(--sheet-crimson-deep) 45%,
        var(--sheet-crimson) 60%,
        var(--sheet-crimson-deep) 66%,
        var(--sheet-lavender) 70%,
        var(--sheet-lavender-light) 88%,
        var(--sheet-lavender) 100%);
  }
  .title {
    margin: 0;
    font-weight: 400;
  }
  .title-lead,
  .title-main {
    position: absolute;
    left: 0;
    right: 0;
    display: block;
    white-space: nowrap;
    color: var(--title-white);
    line-height: 1;
  }
  .title-lead {
    top: 18px;
    font-size: 90px;
    letter-spacing: 0.03em;
  }
  .title-main {
    top: 160px;
    font-size: 200px;
    letter-spacing: 0.01em;
  }
  .tagline {
    position: absolute;
    top: 452px;
    left: 0;
    right: 0;
    margin: 0;
    color: var(--ink-black);
    font-size: 53px;
    line-height: 0.92;
    letter-spacing: 0.02em;
    white-space: nowrap;
  }
  .author {
    position: absolute;
    bottom: 12px;
    left: 0;
    right: 0;
    margin: 0;
    color: var(--ink-black);
    font-size: 80px;
    line-height: 1;
    letter-spacing: 0.03em;
    font-weight: 400;
  }
</style>
</head>
<body>
  <main class="cover">
    <div class="cover-photo" role="img" aria-label="Photograph of crumpled crimson bed sheets over a lavender mattress, with a couple's bare feet intertwined peeking out from beneath the covers"></div>
    <h1 class="title">
      <span class="title-lead">A Quiet Atlas Toward</span>
      <span class="title-main">Closeness</span>
    </h1>
    <p class="tagline">A revolutionary new approach to<br>sexuality, relationship and love.</p>
    <p class="author">Mirela Oswin</p>
  </main>
</body>
</html>
```